Roofing Company Sales Rep Business Card

Business card for sales rep to canvass and hand out to property owners/managers for free roof inspections and roof replacements.

```html
<!DOCTYPE html>
<html lang="en">
<head>
<meta charset="utf-8">
<title>Ridgeline Roofing – Business Card</title>
<link href="https://fonts.googleapis.com/css2?family=Montserrat:wght@400;500;800&display=swap" rel="stylesheet">
<style>
  :root {
    --brand-red: #e31e24;
    --ink: #111111;
    --paper: #ffffff;
    --backdrop: #e6e6e6;
    --muted: #222222;
  }
  * { box-sizing: border-box; margin: 0; padding: 0; }
  html, body {
    width: 1200px; height: 900px; overflow: hidden;
    background: var(--backdrop);
    font-family: 'Montserrat', sans-serif;
  }
  .canvas { position: relative; width: 1200px; height: 900px; }
  .card {
    position: absolute; width: 700px; height: 400px;
    background: var(--paper); border-radius: 26px; overflow: hidden;
    box-shadow: 0 10px 28px rgba(0,0,0,0.18);
  }
  .card--front { left: 60px; top: 40px; }
  .card--back { left: 440px; top: 470px; }

  .wordmark {
    display: flex; align-items: center; gap: 14px;
    font-weight: 800; color: var(--ink); letter-spacing: 1px;
    line-height: 1; white-space: nowrap;
  }
  .wordmark__square { background: var(--brand-red); flex: none; }
  .card--front .wordmark {
    position: absolute; left: 0; right: 0; top: 0; bottom: 0;
    justify-content: center; font-size: 44px;
  }
  .card--front .wordmark__square { width: 34px; height: 34px; }

  .card--back .wordmark {
    position: absolute; left: 32px; top: 152px; font-size: 22px; gap: 12px;
  }
  .card--back .wordmark__square { width: 20px; height: 20px; }

  .divider {
    position: absolute; left: 380px; top: 62px;
    width: 2px; height: 180px; background: var(--brand-red);
  }
  .contact { position: absolute; left: 402px; top: 64px; }
  .contact__name { font-size: 24px; font-weight: 800; color: var(--ink); letter-spacing: 0.5px; white-space: nowrap; }
  .contact__name .surname { color: var(--brand-red); }
  .contact__role { font-size: 14px; font-weight: 500; color: var(--muted); margin: 4px 0 14px; }
  .contact__list { list-style: none; }
  .contact__item {
    display: flex; align-items: center; gap: 10px;
    font-size: 14px; color: var(--muted); margin-bottom: 9px; white-space: nowrap;
  }
  .contact__icon { width: 16px; height: 16px; flex: none; fill: var(--brand-red); }
  .bands { position: absolute; left: 0; bottom: 0; width: 700px; height: 400px; }
</style>
</head>
<body>
<main class="canvas">
  <section class="card card--front" aria-label="Card front">
    <div class="wordmark"><span class="wordmark__square"></span>RIDGELINE ROOFING</div>
  </section>

  <section class="card card--back" aria-label="Card back">
    <svg class="bands" viewBox="0 0 700 400" aria-hidden="true">
      <path d="M0 352 L470 352 C520 352 540 300 560 275 C580 250 610 240 700 240 L700 400 L0 400 Z" fill="var(--brand-red)"/>
      <path d="M0 338 L470 338 C500 338 520 320 535 300 L545 292 C525 325 505 350 470 350 L0 350 Z" fill="var(--ink)"/>
      <path d="M0 350 L470 350 C505 350 525 325 545 292 C560 275 570 268 580 262 C565 285 540 360 470 362 L0 362 Z" fill="var(--paper)"/>
    </svg>

    <div class="wordmark"><span class="wordmark__square"></span>RIDGELINE ROOFING</div>

    <div class="divider"></div>

    <div class="contact">
      <p class="contact__name">DYLAN <span class="surname">MERCER</span></p>
      <p class="contact__role">Co-Founder</p>
      <ul class="contact__list">
        <li class="contact__item">
          <svg class="contact__icon" viewBox="0 0 16 16" aria-hidden="true"><path d="M3 1h3l1.5 4-2 1.3a9 9 0 0 0 4.2 4.2L11 8.5l4 1.5v3a2 2 0 0 1-2 2A12 12 0 0 1 1 3a2 2 0 0 1 2-2z"/></svg>
          843.555.0172
        </li>
        <li class="contact__item">
          <svg class="contact__icon" viewBox="0 0 16 16" aria-hidden="true"><path d="M1 3h14v10H1z"/><path d="M1.5 3.5l6.5 5.5 6.5-5.5" fill="none" stroke="#fff" stroke-width="1.2"/></svg>
          hello@ridgeline-roofs.com
        </li>
        <li class="contact__item">
          <svg class="contact__icon" viewBox="0 0 16 16" aria-hidden="true"><circle cx="8" cy="8" r="7"/><path d="M1 8h14M8 1c3 3 3 11 0 14M8 1c-3 3-3 11 0 14" fill="none" stroke="#fff" stroke-width="1"/></svg>
          www.ridgeline-roofs.com
        </li>
        <li class="contact__item">
          <svg class="contact__icon" viewBox="0 0 16 16" aria-hidden="true"><path d="M8 0a5.5 5.5 0 0 0-5.5 5.5C2.5 10 8 16 8 16s5.5-6 5.5-10.5A5.5 5.5 0 0 0 8 0zm0 8a2.5 2.5 0 1 1 0-5 2.5 2.5 0 0 1 0 5z"/></svg>
          42-15 Harbor Ave 8, Fairview
        </li>
      </ul>
    </div>
  </section>
</main>
</body>
</html>
```